Fern Vale Accounting - New client package

I need a stationary package (presentation folder cover, welcome letter template/design, sample financial report template/design, business card and new logo) for my accounting business. I would like to see designs that use the color blue. Financial icons can be included in the design. The final design should be clean and communicate professionalism and the use of modern; user-friendly technology. Attached postcard files should help with overall design concept.

```html
<!DOCTYPE html>
<html lang="en">
<head>
<meta charset="utf-8">
<title>Fern Vale Accounting – Business Card</title>
<link rel="stylesheet" href="https://fonts.googleapis.com/css2?family=Montserrat:wght@600&family=Roboto:wght@400&family=Saira+Condensed:wght@600&display=swap">
<style>
  :root {
    --stage: #181818;
    --paper: #f8f9fa;
    --brand-blue: #2e5c8a;
    --edge-blue: #a4b6c9;
    --slate: #3b4045;
    --ink: #3a3a3a;
    --white: #ffffff;
  }
  html, body {
    margin: 0;
    width: 1200px;
    height: 1200px;
    overflow: hidden;
    background: var(--stage);
  }
  .card {
    position: absolute;
    left: 318px;
    width: 562px;
    background: var(--paper);
    overflow: hidden;
  }
  .card--front { top: 251px; height: 339px; }
  .card--back  { top: 608px; height: 340px; }

  .brand-dot {
    position: absolute;
    width: 112px;
    height: 112px;
    border-radius: 50%;
    background: var(--brand-blue);
  }
  .wordmark {
    position: absolute;
    font-family: "Montserrat", sans-serif;
    font-weight: 600;
    color: var(--brand-blue);
    text-align: center;
    margin: 0;
    line-height: 1;
  }
  .wordmark span { display: block; }
  .wordmark .name { letter-spacing: 0.02em; }
  .wordmark .trade { letter-spacing: 0.62em; margin-right: -0.62em; }

  /* front */
  .card--front .brand-dot { left: 225px; top: 64px; }
  .card--front .wordmark { left: 0; width: 562px; top: 192px; }
  .card--front .wordmark .name { font-size: 31px; }
  .card--front .wordmark .trade { font-size: 15px; margin-top: 6px; }
  .front-web {
    position: absolute;
    left: 0; width: 562px; top: 433px;
  }
  .web-line {
    position: absolute;
    top: 292px;
    left: 0; width: 562px;
    display: flex;
    justify-content: center;
    align-items: center;
    gap: 14px;
    font-family: "Roboto", sans-serif;
    font-size: 14px;
    color: var(--ink);
  }
  .web-line .dash {
    width: 38px; height: 3px;
    background: var(--brand-blue);
    clip-path: polygon(0 50%, 20% 0, 100% 30%, 100% 70%, 20% 100%);
  }
  .web-line .dash--right { transform: scaleX(-1); }
  .band { position: absolute; bottom: 0; height: 14px; width: 281px; }
  .band--blue { left: 0; background: var(--brand-blue); }
  .band--slate { right: 0; background: var(--slate); }

  /* back */
  .back-panel { position: absolute; inset: 0; }
  .holder {
    position: absolute; left: 34px; top: 46px;
    color: var(--white);
  }
  .holder-name {
    font-family: "Saira Condensed", sans-serif;
    font-weight: 600;
    font-size: 25px;
    line-height: 1;
    margin: 0;
  }
  .holder-role {
    font-family: "Roboto", sans-serif;
    font-size: 14px;
    margin: 6px 0 0;
  }
  .contacts {
    position: absolute; left: 34px; top: 229px;
    list-style: none; margin: 0; padding: 0;
    font-family: "Roboto", sans-serif;
    font-size: 14.5px;
    color: var(--white);
  }
  .contacts li { display: flex; align-items: center; height: 21px; }
  .contacts svg { width: 12px; height: 12px; margin-right: 10px; fill: var(--white); }
  .card--back .brand-dot { left: 369px; top: 93px; }
  .card--back .wordmark { left: 318px; width: 214px; top: 212px; }
  .card--back .wordmark .name { font-size: 24px; }
  .card--back .wordmark .trade { font-size: 11.5px; margin-top: 5px; }
</style>
</head>
<body>

<section class="card card--front">
  <div class="brand-dot"></div>
  <h1 class="wordmark"><span class="name">FERN VALE</span><span class="trade">ACCOUNTING</span></h1>
  <div class="web-line"><span class="dash"></span>www.fernvaleaccounting.com<span class="dash dash--right"></span></div>
  <div class="band band--blue"></div>
  <div class="band band--slate"></div>
</section>

<section class="card card--back">
  <svg class="back-panel" width="562" height="340" viewBox="0 0 562 340">
    <path d="M0 0 H334 Q258 170 344 340 H0 Z" fill="var(--edge-blue)"/>
    <path d="M0 0 H330 Q246 170 330 340 H0 Z" fill="var(--brand-blue)"/>
  </svg>
  <div class="holder">
    <p class="holder-name">Rowan Ellis Hart</p>
    <p class="holder-role">Managing Director</p>
  </div>
  <ul class="contacts">
    <li><svg viewBox="0 0 12 12"><path d="M1 4 Q6 0 11 4 L9.5 5.5 L8 4.5 L8 3.6 Q6 3 4 3.6 L4 4.5 L2.5 5.5 Z M3 6 H9 L10 11 H2 Z"/></svg>1.877.555.0142</li>
    <li><svg viewBox="0 0 12 12"><path d="M0 2 H12 V10 H0 Z M1 3 L6 7 L11 3 V3 Z" fill-rule="evenodd"/></svg>info@fernvaleaccounting.com</li>
    <li><svg viewBox="0 0 12 12"><circle cx="6" cy="6" r="5.2" fill="none" stroke="#fff" stroke-width="1"/><ellipse cx="6" cy="6" rx="2.2" ry="5.2" fill="none" stroke="#fff" stroke-width="1"/><path d="M1 6 H11 M2 3.5 H10 M2 8.5 H10" stroke="#fff" stroke-width="0.9"/></svg>www.fernvaleaccounting.com</li>
  </ul>
  <div class="brand-dot"></div>
  <h2 class="wordmark"><span class="name">FERN VALE</span><span class="trade">ACCOUNTING</span></h2>
</section>

</body>
</html>
```